Building and Facilities Management brochure

Please refer to attached PDF, page by page with information about the brief.
SOPHISTICATED, BOLD, PROFESSIONAL BROCHURE to market our company in business meetings to Builders, Owners of buildings, Strata Committees etc.

The final design should portray quality, service, integrity,
Clear Communication

Attached is:
- pdf with details of basic layout options and wording and most of the information about the brief.
- Logo options to use
- Business card designs to understand what design we have previously had.
- Word document of the pdf if that helps to copy the information.

Target Market(s)

Professionals. Builders/developer, Strata Owners, and Building owners who want a high level of service and management of their building

Industry/Entity Type

It Company

Requirements
Must have
• - Logo
• - Contact details
• - Use of the colour in the design which has been specified.
• - Images/s of building/s
• - Use the phrase "Quality Service with Integrity"
Nice to have
• - as much of the wording as possible from the document which was uploaded, that will fit and work with the design
Should not have
• Excessive colour or variances as it needs to stay clear, bold and sophisticated.
• Too much on the page, clarity is key for clear communication without trying to clutter too much on the page.

```html
<!DOCTYPE html>
<html lang="en">
<head>
<meta charset="utf-8">
<title>Halden Building and Facilities Management Brochure</title>
<link href="https://fonts.googleapis.com/css2?family=Open+Sans:wght@400;600;700&display=swap" rel="stylesheet">
<style>
  :root {
    --backdrop: #2b2b2d;
    --panel: #3a3b3e;
    --panel-deep: #333437;
    --accent: #4a90d9;
    --accent-text: #5aa6ee;
    --text: #e2e2e2;
    --text-soft: #c4c4c4;
    --photo-sky: #c9d2dc;
    --photo-city: #6f7a86;
    --photo-green: #5d7048;
    --photo-water: #4d5e6c;
  }
  * { box-sizing: border-box; margin: 0; padding: 0; }
  html, body { width: 1200px; height: 789px; overflow: hidden; }
  body {
    background: var(--backdrop);
    font-family: "Open Sans", Arial, sans-serif;
    color: var(--text);
  }
  .spread {
    position: absolute; left: 50px; top: 45px;
    width: 1100px; height: 700px;
    box-shadow: 0 12px 40px rgba(0,0,0,.55);
    overflow: hidden;
  }
  .city-photo {
    position: absolute; inset: 0;
    background: linear-gradient(180deg, var(--photo-sky) 0%, #aeb9c6 30%, var(--photo-city) 50%, var(--photo-green) 72%, var(--photo-water) 100%);
  }
  .spine {
    position: absolute; left: 549px; top: 0; width: 2px; height: 100%;
    background: linear-gradient(90deg, rgba(0,0,0,.35), rgba(255,255,255,.15));
  }
  .panel {
    position: absolute;
    background: var(--panel);
  }
  .tab {
    position: absolute;
    background: var(--accent);
    color: #fff;
    font-size: 17px; font-weight: 400; letter-spacing: 1px;
    text-transform: uppercase;
    padding: 6px 28px;
  }
  .body-copy { font-size: 11.5px; line-height: 1.45; color: var(--text-soft); }
  .body-copy p + p { margin-top: 10px; }
  .accent { color: var(--accent-text); font-weight: 600; }

  /* Vision */
  .vision-panel { left: 40px; top: 40px; width: 510px; height: 220px; padding: 46px 36px 20px 40px; }
  .vision-panel .tab { left: 70px; top: -14px; }

  /* Key aspects */
  .aspects-panel { left: 0; top: 410px; width: 530px; height: 250px; padding: 44px 28px 20px 34px; }
  .aspects-panel .tab { left: 110px; top: -18px; }
  .aspects-list { list-style: none; font-size: 10.5px; line-height: 1.4; color: var(--text-soft); }
  .aspects-list li + li { margin-top: 4px; }

  /* Services */
  .services-panel { left: 570px; top: 130px; width: 510px; height: 220px; padding: 44px 30px 20px 36px; }
  .services-panel .tab { left: 60px; top: -16px; }
  .services-intro { font-size: 11px; color: var(--text-soft); line-height: 1.4; }
  .services-intro .accent { display: block; font-size: 12px; }
  .core-services { display: flex; justify-content: space-around; margin-top: 18px; }
  .core-service { text-align: center; width: 110px; font-size: 12px; color: var(--text); }
  .core-service svg { display: block; margin: 0 auto 8px; }

  /* Value added */
  .value-panel { left: 570px; top: 450px; width: 510px; height: 225px; padding: 34px 22px 20px 30px; display: flex; gap: 20px; }
  .value-copy { width: 200px; flex: none; font-size: 11px; line-height: 1.45; color: var(--text-soft); }
  .value-copy .accent { display: block; font-size: 12.5px; margin-bottom: 2px; }
  .value-list { list-style: none; font-size: 14px; color: var(--text); flex: none; }
  .value-list li { display: flex; align-items: center; gap: 8px; line-height: 1.55; white-space: nowrap; }
</style>
</head>
<body>
<main class="spread">
  <div class="city-photo" role="img" aria-label="Photograph of a city skyline with office towers, a white arched footbridge over a river and trees along the bank"></div>
  <div class="spine"></div>

  <section class="panel vision-panel">
    <h2 class="tab">Vision</h2>
    <div class="body-copy">
      <p>At Halden, our aim is to provide complete solutions for Building and Facilities Owners and Strata Corporations in the management of their assets. With the understanding that each property has different needs and requirements, our focus is to work with clients to tailor solutions best suited to their specific needs.</p>
      <p>Our aim is to ensure the Building and Facilities are managed to the highest standards using the latest technological management solutions to efficiently and effectively control all aspects of the building. With a keen focus on controlling costs to ensure funds are spent cost-effectively, through improved operations and management of all aspects of the building.</p>
    </div>
  </section>

  <section class="panel aspects-panel">
    <h2 class="tab">Key Aspects:</h2>
    <ul class="aspects-list">
      <li><span class="accent">Compliance</span> – with relevant industry acts and regulations</li>
      <li><span class="accent">OH&amp;S</span> – to ensure the building and aspects are controlled safely and the risk of all contractors and owners is reduced and managed.</li>
      <li><span class="accent">Preventative Maintenance</span> – to ensure assets are professionally maintained to ensure the best reliability and longevity of each asset.</li>
      <li><span class="accent">Reactive Maintenance</span> – to ensure any issues that arise are resolved and handled as efficiently as possible.</li>
      <li><span class="accent">Communication</span> – to ensure the Committee and Owners have clear and concise information and knowledge of the aspects of their building and assets.</li>
      <li><span class="accent">Relationships</span> – are a top priority as they are paramount for effective management with Owners, Residents, Developers and Strata Managers.</li>
    </ul>
  </section>

  <section class="panel services-panel">
    <h2 class="tab">Services</h2>
    <p class="services-intro"><span class="accent">Core Services</span>These are the core focus of the business to provide the highest standard in Building and Facilities Management.</p>
    <div class="core-services">
      <div class="core-service">
        <svg width="52" height="56" viewBox="0 0 52 56"><polygon points="26,2 49,15 49,41 26,54 3,41 3,15" fill="var(--panel-deep)" stroke="var(--accent)" stroke-width="1.5"/><rect x="18" y="18" width="16" height="22" fill="#fff"/><g fill="var(--accent)"><rect x="21" y="22" width="3" height="3"/><rect x="28" y="22" width="3" height="3"/><rect x="21" y="28" width="3" height="3"/><rect x="28" y="28" width="3" height="3"/><rect x="24" y="34" width="4" height="6"/></g></svg>
        Building Management
      </div>
      <div class="core-service">
        <svg width="52" height="56" viewBox="0 0 52 56"><polygon points="26,2 49,15 49,41 26,54 3,41 3,15" fill="var(--panel-deep)" stroke="var(--accent)" stroke-width="1.5"/><rect x="15" y="16" width="12" height="24" fill="#fff"/><rect x="27" y="24" width="11" height="16" fill="var(--accent)"/><g fill="var(--panel-deep)"><rect x="18" y="20" width="2.5" height="3"/><rect x="22" y="20" width="2.5" height="3"/><rect x="18" y="26" width="2.5" height="3"/><rect x="22" y="26" width="2.5" height="3"/></g></svg>
        Facilities Management
      </div>
      <div class="core-service">
        <svg width="52" height="56" viewBox="0 0 52 56"><polygon points="26,2 49,15 49,41 26,54 3,41 3,15" fill="var(--panel-deep)" stroke="var(--accent)" stroke-width="1.5"/><rect x="16" y="24" width="20" height="14" rx="2" fill="#fff"/><path d="M21 24v-4h10v4" fill="none" stroke="#fff" stroke-width="2"/><rect x="16" y="29" width="20" height="2" fill="var(--accent)"/></svg>
        Caretaker
      </div>
    </div>
  </section>

  <section class="panel value-panel">
    <p class="value-copy"><span class="accent">Value Added Services</span>In addition to the Core Service we are proud to offer these Value-Added services to complement the management of the Building or offer as stand-alone services to assist owners with the management of their Building and Assets.</p>
    <ul class="value-list">
      <li><svg width="12" height="10" viewBox="0 0 12 10"><path d="M1 5l3.5 3.5L11 1" fill="none" stroke="var(--accent-text)" stroke-width="2"/></svg>Concierge</li>
      <li><svg width="12" height="10" viewBox="0 0 12 10"><path d="M1 5l3.5 3.5L11 1" fill="none" stroke="var(--accent-text)" stroke-width="2"/></svg>Cleaning</li>
      <li><svg width="12" height="10" viewBox="0 0 12 10"><path d="M1 5l3.5 3.5L11 1" fill="none" stroke="var(--accent-text)" stroke-width="2"/></svg>Project Management</li>
      <li><svg width="12" height="10" viewBox="0 0 12 10"><path d="M1 5l3.5 3.5L11 1" fill="none" stroke="var(--accent-text)" stroke-width="2"/></svg>Electrical</li>
      <li><svg width="12" height="10" viewBox="0 0 12 10"><path d="M1 5l3.5 3.5L11 1" fill="none" stroke="var(--accent-text)" stroke-width="2"/></svg>Handyman</li>
      <li><svg width="12" height="10" viewBox="0 0 12 10"><path d="M1 5l3.5 3.5L11 1" fill="none" stroke="var(--accent-text)" stroke-width="2"/></svg>New site setup</li>
      <li><svg width="12" height="10" viewBox="0 0 12 10"><path d="M1 5l3.5 3.5L11 1" fill="none" stroke="var(--accent-text)" stroke-width="2"/></svg>Building defect management</li>
    </ul>
  </section>
</main>
</body>
</html>
```